New boutique IT consultancy needs business card

I need a business card and logo for my IT consultancy business, called 'Quenbrylle' . I want it to make me look bigger than I am. I want it to look classy, and modern. Simple design, that will be easy for me to translate into my webpage etc. The business card should be bold, and different.

The logo should emphasise the 'y' as used in quenbrylle

Target Market(s)

IT divisions in other companies

Industry/Entity Type

Business

Contact Information for Business Card

Marcel Thornby
Director
+61 437 819 063
mthornby@quenbrylle-mail.com

```html
<!DOCTYPE html>
<html lang="en">
<head>
<meta charset="utf-8">
<title>Quenbrylle — Business Card</title>
<link rel="stylesheet" href="https://fonts.googleapis.com/css2?family=Montserrat:wght@300;400;600&display=swap">
<style>
  :root {
    --ink: #1e1e1e;
    --paper: #ffffff;
    --accent: #ef5323;
    --text: #3a3a3a;
    --backdrop: #e9e7e4;
  }
  * { box-sizing: border-box; margin: 0; padding: 0; }
  html, body {
    width: 1200px;
    height: 799px;
    overflow: hidden;
  }
  body {
    background: var(--backdrop);
    font-family: "Montserrat", Arial, sans-serif;
    position: relative;
  }
  .card {
    position: absolute;
    top: 240px;
    width: 520px;
    height: 318px;
    background: var(--paper);
    overflow: hidden;
    box-shadow: 0 6px 18px rgba(0,0,0,0.18);
  }

  /* Back of card */
  .card--back { left: 60px; background: var(--ink); }
  .brand-band {
    position: absolute;
    left: 0; right: 0;
    top: 92px;
    height: 140px;
    background: var(--paper);
    display: flex;
    align-items: center;
    justify-content: center;
    gap: 14px;
  }
  .brand-band::before,
  .brand-band::after {
    content: "";
    position: absolute;
    left: 0; right: 0;
    height: 2px;
    background: var(--accent);
  }
  .brand-band::before { top: 9px; }
  .brand-band::after { bottom: 9px; }
  .brand-mark {
    width: 34px;
    height: 34px;
    background: var(--accent);
  }
  .brand-name {
    font-weight: 600;
    font-size: 34px;
    letter-spacing: 3px;
    text-transform: uppercase;
    color: var(--ink);
  }

  /* Front of card */
  .card--front { left: 620px; }
  .corner-block {
    position: absolute;
    left: 0; top: 30px;
    width: 76px; height: 22px;
    background: var(--ink);
  }
  .rule {
    position: absolute;
    left: 0; right: 0;
    height: 2px;
    background: var(--accent);
  }
  .rule--top { top: 52px; }
  .rule--bottom { top: 152px; }
  .identity {
    position: absolute;
    left: 48px;
    top: 78px;
    color: var(--text);
  }
  .identity__name {
    font-weight: 400;
    font-size: 25px;
    letter-spacing: 0.5px;
    text-transform: uppercase;
    line-height: 1.1;
  }
  .identity__role {
    font-weight: 400;
    font-size: 17px;
    margin-left: 8px;
    margin-top: 2px;
  }
  .side-panel {
    position: absolute;
    left: 0; top: 158px;
    width: 128px; height: 160px;
  }
  .contacts {
    position: absolute;
    left: 150px;
    top: 182px;
    list-style: none;
    color: var(--text);
    font-size: 12.5px;
    font-weight: 400;
  }
  .contacts li {
    display: flex;
    align-items: center;
    gap: 16px;
    height: 20px;
    margin-bottom: 22px;
  }
  .contacts svg { width: 17px; height: 17px; flex: none; }
</style>
</head>
<body>

  <section class="card card--back" aria-label="Card back">
    <div class="brand-band">
      <span class="brand-mark"></span>
      <span class="brand-name">Quenbrylle</span>
    </div>
  </section>

  <section class="card card--front" aria-label="Card front">
    <div class="corner-block"></div>
    <div class="rule rule--top"></div>
    <div class="identity">
      <p class="identity__name">Marcel Thornby</p>
      <p class="identity__role">Director</p>
    </div>
    <div class="rule rule--bottom"></div>

    <svg class="side-panel" viewBox="0 0 128 160" aria-hidden="true">
      <polygon points="0,0 110,0 128,160 0,160" fill="var(--ink)"/>
      <rect x="62" y="35" width="22" height="2.5" fill="var(--paper)"/>
      <rect x="62" y="77" width="22" height="2.5" fill="var(--paper)"/>
    </svg>

    <ul class="contacts">
      <li>
        <svg viewBox="0 0 24 24" aria-hidden="true">
          <path fill="var(--accent)" d="M6.6 10.8a15.1 15.1 0 0 0 6.6 6.6l2.2-2.2c.3-.3.7-.4 1-.2 1.1.4 2.3.6 3.6.6.6 0 1 .4 1 1V20c0 .6-.4 1-1 1A17 17 0 0 1 3 4c0-.6.4-1 1-1h3.5c.6 0 1 .4 1 1 0 1.3.2 2.5.6 3.6.1.3 0 .7-.2 1z"/>
        </svg>
        <span>+61 437 819 063</span>
      </li>
      <li>
        <svg viewBox="0 0 24 24" aria-hidden="true">
          <circle cx="12" cy="12" r="11" fill="var(--accent)"/>
          <g fill="none" stroke="var(--paper)" stroke-width="1.3">
            <circle cx="12" cy="12" r="7"/>
            <ellipse cx="12" cy="12" rx="3" ry="7"/>
            <line x1="5" y1="12" x2="19" y2="12"/>
          </g>
        </svg>
        <span>mthornby@quenbrylle-mail.com</span>
      </li>
    </ul>
  </section>

</body>
</html>
```